Web Design Project HopeHaven - Design+Coding

HopeHaven-Temecula needs a new website! Design + Coding required.

This church is looking for a highly designed, highly interactive web platform from which to launch their ministry.

We're looking for a highly creative web developer that can grasp the vision for this site and take ownership of the development to conceive engaging additional details and elements for the site.

A cookie cutter website template just won't do it for this one. Even though the initial site is not large, it should feel highly designed and highly engaging. In the words of their Senior Pastor: “We want people to realize that if we care this much about a website, imagine how much more we're going care about their family!”

Details: HopeHaven - Temecula is a new church plant in Temecula, CA built on a self-replicating "missionary" model. Essentially, the goal is to attract people, point them to Christ, develop them into mature Christians and send them out to plant churches as part of church plant "teams". This model resembles more of what is done overseas then in the USA.

As well, the Church is what is called "Family Integrated" which means that it ministers to the family as well as the individual. That means children and parents attend services together as a family unit. As such, the site needs to be "family friendly" and welcoming.

The Logo files are attached. They do not need to drive the palette of the site per se but the logo should look like it "belongs" on the site.

Website has 6 main landing pages with limited add'l content pages.

No Flash. Should look good on mobile as well as traditional browser.

Should be "scalable" - easy to expand nav bars, pages, etc as the church grows with ability to add plug ins (like Google maps or iTunes podcast downloads).

PLEASE SEE ATTACHED DOCUMENT: HH-T Website Info.doc for more details.

Logo File attached below.

Use your imagination! Have fun... design a church website that you would want to visit and interact with. If you think of things we might have missed that add great functionality, value, uniqueness or enhance user experience, add them!!! God bless!

Another Marlowe Studios Inc/Pixel Forum Job. Thanks again Designers!

• Must be a fully coded, functional website.

Site must be tested and good to go in IE 7+, Firefox 9+, Chrome and both Apple and Android Mobile platforms.

Blog must be one that church can easily upload content to as an integrated part of the site (no Postwright.example, etc plugins please).

Final handover must include full rights to the designs, stock art, coding, etc (so, no "one use templates" please).

Must be a user-scalable platform on a user friendly CMS (CMS is designers choice so long as it is industry standard and user friendly). We want the church to be able to add or modify page elements themselves.

Final handover will include loading and testing on to our hosting server.

The designer must be willing to support the site for 30 days after launch as part of the site payment.
• Prefer a custom designed template (should not look like a "cookie cutter" site).

See attached doc for more!
• Any non-standard CMS or industry unsupported plugins.

No Flash.

```html
<!DOCTYPE html>
<html lang="en">
<head>
<meta charset="utf-8">
<title>HopeHaven Temecula – We Are</title>
<link href="https://fonts.googleapis.com/css2?family=PT+Sans:ital,wght@0,400;0,700;1,700&family=Oswald:wght@500&display=swap" rel="stylesheet">
<style>
:root{
  --page-top:#e4e4e4;
  --page-mid:#cfcfcf;
  --card:#f6f6f6;
  --card-edge:#d6d6d6;
  --nav:#b5432a;
  --nav-edge:#8a2e1c;
  --nav-text:#ffffff;
  --nav-active:#f6c51b;
  --nav-cta:#d7e03a;
  --heading-blue:#3a68a6;
  --heading-brown:#5a3718;
  --body:#444444;
  --link:#b5432a;
  --bullet:#e7a84a;
  --footer:#6b1c4b;
  --footer-text:#ffffff;
  --footer-soft:#d3b2c5;
  --footer-gold:#f5c51b;
  --footer-lime:#c9d93b;
}
*{margin:0;padding:0;box-sizing:border-box}
html,body{width:1200px;height:1081px;overflow:hidden}
body{position:relative;font-family:"PT Sans",sans-serif;color:var(--body);
  background:linear-gradient(to bottom,#f1f1f1 0,var(--page-top) 244px,#c9c9c9 246px,#d9d9d9 480px,#f4f4f4 760px,#ffffff 839px);}
.abs{position:absolute}
.brand{left:130px;top:52px;display:flex;align-items:center;gap:10px;font-size:34px;font-weight:700;color:#555}
.brand-mark{width:60px;height:60px;border-radius:50%;background:#3a68a6}
.nav{left:431px;top:57px;width:640px;height:43px;background:var(--nav);border:1px solid var(--nav-edge);
  box-shadow:0 10px 12px -8px rgba(0,0,0,.45);}
.nav a{position:absolute;top:9px;font-family:"Oswald",sans-serif;font-size:16px;color:var(--nav-text);text-decoration:none;letter-spacing:.3px;text-shadow:0 1px 1px rgba(0,0,0,.4)}
.nav a.active{color:var(--nav-active)}
.nav a.cta{color:var(--nav-cta)}
.card{left:129px;top:144px;width:942px;height:681px;background:var(--card);border:1px solid var(--card-edge);border-radius:4px;box-shadow:0 0 0 3px #ececec,0 2px 8px rgba(0,0,0,.15)}
.page-title{left:162px;top:176px;font-size:30px;font-weight:700;color:var(--heading-blue)}
.about{left:162px;top:222px;width:576px;font-size:13px;line-height:20px}
.about-photo{float:left;width:188px;height:215px;margin:4px 20px 8px 1px;border-radius:3px;background:linear-gradient(135deg,#8a7a5a,#6c6f6a 50%,#b0a9a0)}
.about h2{font-size:18px;font-weight:700;color:var(--heading-brown);margin:0 0 8px;line-height:22px}
.about p{margin-bottom:7px}
.divider-v{left:748px;top:183px;height:580px;border-left:1px dashed #b5b5b5}
.divider-h{border-top:1px dashed #b5b5b5}
.btn{display:flex;align-items:center;justify-content:center;width:99px;height:28px;border-radius:3px;background:linear-gradient(#444,#0d0d0d);color:#fff;font-size:12.5px;letter-spacing:.3px}
.side-title{left:777px;top:180px;font-size:24px;font-weight:700;color:var(--heading-blue)}
.side-photo{left:778px;top:225px;width:273px;height:122px;border-radius:4px;background:radial-gradient(ellipse at 50% 40%,#f7b548,#d9561c 55%,#7a1f0a)}
.side-text{left:778px;top:358px;width:275px;font-size:13px;line-height:20px}
.side-list{left:778px;top:446px;width:275px;list-style:none;font-size:13px;line-height:20px}
.side-list li{position:relative;padding-left:20px;margin-bottom:8px;color:var(--link)}
.side-list li::before{content:"";position:absolute;left:1px;top:7px;width:7px;height:7px;border-radius:50%;background:var(--bullet)}
.footer{left:0;top:839px;width:1200px;height:242px;background:var(--footer);color:var(--footer-text)}
.footer h3{position:absolute;top:16px;font-size:18px;font-weight:700}
.blog-text{left:131px;top:49px;width:225px;font-size:13px;line-height:20px}
.continue{left:131px;top:124px;font-size:12px;font-style:italic;font-weight:700;color:var(--footer-lime)}
.read-all{left:265px;top:164px;font-size:12px;text-decoration:underline}
.loc{left:413px;top:52px;width:300px;font-size:12.5px;line-height:20px;color:var(--footer-gold)}
.loc .name{font-size:15px;font-weight:700;margin-bottom:2px}
.loc .label{color:var(--footer-text);font-weight:700}
.social{left:738px;top:46px;list-style:none;font-size:13px;color:var(--footer-soft)}
.social li{display:flex;align-items:center;gap:11px;height:26px}
.social svg{width:16px;height:16px}
.badge{left:1001px;top:44px;width:69px;height:84px;background:#f2f2f2}
.badge::after{content:"";position:absolute;left:0;top:24px;width:69px;height:16px;background:#2f6fbf}
.foot-brand{left:895px;top:146px;display:flex;align-items:center;gap:8px;font-size:24px;font-weight:700;color:#d9d0d5}
.foot-brand span{width:34px;height:34px;border-radius:50%;background:#d9d0d5}
.copy{right:130px;top:206px;font-size:11px}
</style>
</head>
<body>
<div class="abs brand"><span class="brand-mark"></span>HopeHaven</div>

<nav class="abs nav">
  <a style="left:16px">HOME</a>
  <a class="active" style="left:84px">WE ARE</a>
  <a style="left:164px">GIVE</a>
  <a style="left:227px">PASTOR</a>
  <a style="left:309px">BLOG</a>
  <a style="left:374px">BELIVE</a>
  <a style="left:447px">CONTACT</a>
  <a class="cta" style="left:537px">KNOW JESUS?</a>
</nav>

<div class="abs card"></div>

<h1 class="abs page-title">WE ARE</h1>
<article class="abs about">
  <div class="about-photo" role="img" aria-label="Photo of a young family walking outdoors together"></div>
  <h2>We Are… not your “average” Church</h2>
  <p>&nbsp;It’s easy for a church to tell you what they’re not.&nbsp; Let us instead tell you who we are!</p>
  <p>HopeHaven-Temecula was formed with a very simple goal: Look at what the Church is called to be in Scripture and then live that our here in 21st century Temecula, CA.</p>
  <p>We aim to invite people in, see them transformed by the power of Christ, discipled into mature ambassadors and sent out to proclaim the truth of Christ to a world that needs to hear it.</p>
  <p>Truthfully, we’re not going to look like an “average American church” and we hope to never be one! We don’t want to be bogged down with committees and mortgages and strangled by debt.&nbsp; We want to be a vibrant, active body of believers that Paul or Peter or John would look at and say “hey, now there are some people that love Jesus”.</p>
  <p>Is it possible?&nbsp; We think so… In fact, the Bible tells us how to do it.</p>
  <p>Imagine for a second a place where the only focus was Christ.&nbsp; Not the upcoming potluck.&nbsp; Not the children’s choir, softball tournament or the next youth carwash.&nbsp; Just Christ.</p>
  <p>Imagine a gathering where the focus of every activity was evangelism, discipleship, fellowship and/or worship.&nbsp; Simply a meeting together of people who are being challenged to know Christ, grow in Christ and share Christ with their world.</p>
  <p>It’s not impossible… in fact it is the norm for Christians all over the world; despite how foreign it seems here in America.</p>
</article>
<div class="abs divider-h" style="left:160px;top:745px;width:555px"></div>
<a class="abs btn" style="left:159px;top:755px">READ MORE</a>

<div class="abs divider-v"></div>

<h2 class="abs side-title">Know Jesus</h2>
<div class="abs side-photo" role="img" aria-label="Wooden cross against a glowing orange sunset sky"></div>
<p class="abs side-text">Here at HopeHaven, we are committed to one truth – Jesus Christ, Savior of the world.&nbsp; Our goal is not to persuade or cajole, simply to present the Truth outlined in Scripture:</p>
<ul class="abs side-list">
  <li>Did you accept Jesus Christ as YOUR Lord and Savior?</li>
  <li>Who is Jesus ?</li>
  <li>Why do i need Jesus ?</li>
  <li>So, How do we fix this ?</li>
  <li>How do I get this forgiveness and new life?</li>
  <li>What happens if I don’t accept Jesus?</li>
</ul>
<div class="abs divider-h" style="left:778px;top:654px;width:268px"></div>
<a class="abs btn" style="left:779px;top:664px">READ MORE</a>

<footer class="abs footer">
  <h3 style="left:130px">Latest Blog Post</h3>
  <p class="abs blog-text">Lorem ipsum dolor sit amet, consecte-tur adipiscing elit. Fusce accumsan, elit a suscipit sagittis ac nulla.....</p>
  <span class="abs continue">Continue Reading</span>
  <span class="abs read-all">READ ALL POST</span>

  <h3 style="left:412px">Our Location</h3>
  <div class="abs loc">
    <div class="name">HopeHaven Temecula</div>
    <div style="font-weight:700">Service Location:</div>
    <div style="margin-top:4px">Vista 10 Cinemas – Temecula CA (Right off Route 9 at the corner of Oak Meadow and Linden Rd)</div>
    <div style="margin-top:4px"><span class="label">Phone:</span>&nbsp; 555.014.2260</div>
    <div style="margin-top:4px"><span class="label">Email:</span>&nbsp; hello@hopehaven-temecula.example</div>
    <div style="margin-top:4px"><span class="label">Website:</span>&nbsp; hopehaven-temecula.example</div>
  </div>

  <h3 style="left:737px">Footer Link</h3>
  <ul class="abs social">
    <li><svg viewBox="0 0 16 16"><rect width="16" height="16" rx="2" fill="#3b5a9a"/></svg>Friendwall</li>
    <li><svg viewBox="0 0 16 16"><rect width="16" height="16" rx="2" fill="#3aa3d8"/></svg>Chirper</li>
    <li><svg viewBox="0 0 16 16"><rect width="16" height="16" rx="2" fill="#2a76b0"/></svg>Worknet</li>
    <li><svg viewBox="0 0 16 16"><rect width="16" height="16" rx="2" fill="#f18a1e"/><circle cx="4.5" cy="11.5" r="1.6" fill="#fff"/><path d="M3 7a6 6 0 0 1 6 6M3 3.5a9.5 9.5 0 0 1 9.5 9.5" stroke="#fff" stroke-width="1.8" fill="none"/></svg>Rss Feed</li>
    <li><svg viewBox="0 0 16 16"><rect width="16" height="16" rx="2" fill="#c4302b"/></svg>Vidstream</li>
  </ul>

  <h3 style="right:130px">Account With</h3>
  <div class="abs badge" role="img" aria-label="Partner certification badge"></div>
  <div class="abs foot-brand"><span></span>HopeHaven</div>
  <p class="abs copy">© Copyright 2013. All Right Reserved</p>
</footer>
</body>
</html>
```